Bright Canyon, LLC Business Card Design

We need a product business card designed for a new company Bright Canyon, LLC. We make and resell waterless RV cleaner, polish and protectant. It cleans and protects in a simple spray and wipe step leaving the surface protected and conditioned to repel dust, dirt, water, smudges, bugs and fingerprints while preventing fogging. Safe on acrylic, clarisheet, durvane, plastic, rubber, painted surfaces, chrome, stainless, aluminum, vinyl, leather, glass.... This is an eco-friendly green product.

We want to play off the company name to tell the consumer that the product is easy to use and associate to the nostalgics 1950's in the USA... Thinking old travel trailer with hot rod truck pulling it as the graphic, maybe the husband cleaning the truck and the wife cleaning the trailer for a Bright Canyon surface.
Updates

Just posted our newly finished logo. Need to have "Cleaner and Protectant" added to the design as well. Thanks everyone that has submitted thus far, i am working to get comments on all.

If you need a different file format, please let me know. Thank you.

Most important info, is the logo, website and the words "Cleaner" or "Clean" along "Protectant" or "Protect" the remainder is of less importance. Highlight: www.brightcanyoncleaner.example Focus is on company brand for Brighter Canyon Cleaner product: However, need a section for the following contact info: John Doe (xxx) xxx-xxxx email address Would like space for QR Code if possible.

Target Market(s)

Adults in the USA between ages of 35-75 that are actively involved in the Recreational Vehicle (RV), travel trailer, and hot rod lifestyle. We are targeting the RV marked of the high end travel, 5th wheel and bus RV market. Along with hot rods, automotive and motorcycle market.

Industry/Entity Type

Travel

Requirements
Must have
• Most important info, is the logo, website and the words "Cleaner" or "Clean" along "Protectant" or "Protect" the remainder is of less importance.

Highlight:
www.brightcanyoncleaner.example

Focus is on company brand for Brighter Canyon Cleaner product: However, need a section for the following contact info:

John Doe
(xxx) xxx-xxxx
email address
Nice to have
• Would like a space for a QR Code.

```html
<!DOCTYPE html>
<html lang="en">
<head>
<meta charset="utf-8">
<title>Bright Canyon, LLC – Business Card</title>
<link rel="stylesheet" href="https://fonts.googleapis.com/css2?family=Saira:wght@300;400;700&display=swap">
<style>
  :root {
    --stage: #e6e8eb;
    --card-white: #ffffff;
    --card-shade: #e4e6e8;
    --band-grey: #4a4c50;
    --blue-light: #3f9ae6;
    --blue-deep: #1565c8;
    --ink: #1d1f22;
    --ink-soft: #55585d;
    --on-blue: #ffffff;
    --retro-sky: #9fd0f0;
    --retro-sand: #e8c99a;
  }
  * { box-sizing: border-box; margin: 0; padding: 0; }
  html, body {
    width: 1200px;
    height: 900px;
    overflow: hidden;
    background: var(--stage);
    font-family: "Saira", sans-serif;
  }
  .sheet {
    width: 1200px;
    height: 900px;
    display: flex;
    flex-direction: column;
    align-items: center;
    justify-content: center;
    gap: 50px;
  }
  .card {
    position: relative;
    width: 700px;
    height: 400px;
    border-radius: 34px;
    overflow: hidden;
    background: linear-gradient(135deg, var(--card-white) 40%, var(--card-shade));
    box-shadow: 0 10px 26px rgba(0, 0, 0, 0.18);
  }
  .card-art {
    position: absolute;
    inset: 0;
    width: 100%;
    height: 100%;
  }
  .brand-name {
    font-family: "Saira", sans-serif;
    font-weight: 700;
    text-transform: uppercase;
    color: var(--ink);
    letter-spacing: 0.5px;
    white-space: nowrap;
  }
  .product-line {
    font-weight: 400;
    text-transform: uppercase;
    color: var(--ink-soft);
    letter-spacing: 2px;
    white-space: nowrap;
  }
  .front-brand {
    position: absolute;
    top: 54px;
    left: 40px;
  }
  .front-brand .brand-name { font-size: 30px; line-height: 1.1; }
  .front-brand .product-line { font-size: 12px; margin-top: 4px; }

  .contact {
    position: absolute;
    right: 46px;
    top: 54px;
    text-align: right;
    color: var(--on-blue);
  }
  .contact-name {
    font-size: 26px;
    font-weight: 400;
    letter-spacing: 2px;
    text-transform: uppercase;
  }
  .contact-role {
    font-size: 15px;
    font-weight: 300;
    margin-top: 2px;
  }
  .contact-address {
    font-size: 16px;
    font-weight: 300;
    line-height: 1.35;
    margin-top: 26px;
  }
  .contact-lines {
    list-style: none;
    margin-top: 30px;
    font-size: 15px;
    font-weight: 300;
    line-height: 1.9;
  }
  .contact-lines li {
    display: flex;
    justify-content: flex-end;
    align-items: center;
    gap: 10px;
  }
  .contact-lines .website { font-weight: 400; }
  .icon {
    width: 15px;
    height: 15px;
    fill: none;
    stroke: var(--on-blue);
    stroke-width: 1.8;
    stroke-linecap: round;
    stroke-linejoin: round;
  }

  .back-brand {
    position: absolute;
    top: 92px;
    left: 50px;
  }
  .back-brand .brand-name { font-size: 52px; line-height: 1.05; }
  .back-brand .product-line { font-size: 18px; margin-top: 8px; }
  .back-brand .back-website {
    font-size: 17px;
    font-weight: 400;
    color: var(--blue-deep);
    margin-top: 18px;
  }
  .qr-space {
    position: absolute;
    top: 92px;
    right: 50px;
    width: 120px;
    height: 120px;
    border: 2px solid var(--band-grey);
    border-radius: 6px;
    background: var(--card-white);
  }
  .retro-scene {
    position: absolute;
    left: 0;
    right: 0;
    bottom: 0;
    height: 96px;
    background: linear-gradient(180deg, var(--retro-sky), var(--blue-light) 55%, var(--retro-sand) 56%, var(--retro-sand));
    opacity: 0.85;
  }
</style>
</head>
<body>
<main class="sheet">

  <section class="card card-front" aria-label="Business card front">
    <svg class="card-art" viewBox="0 0 700 400" preserveAspectRatio="none" aria-hidden="true">
      <defs>
        <linearGradient id="blueField" x1="0" y1="1" x2="1" y2="0">
          <stop offset="0" stop-color="var(--blue-deep)"/>
          <stop offset="1" stop-color="var(--blue-light)"/>
        </linearGradient>
      </defs>
      <path class="curve-band" fill="var(--band-grey)"
            d="M0,205 C190,175 360,105 405,0 L450,0 C395,125 210,200 0,240 Z"/>
      <path class="blue-field" fill="url(#blueField)"
            d="M0,240 C210,200 395,125 450,0 L700,0 L700,400 L0,400 Z"/>
    </svg>

    <div class="front-brand">
      <p class="brand-name">Bright Canyon</p>
      <p class="product-line">Cleaner &amp; Protectant</p>
    </div>

    <div class="contact">
      <p class="contact-name">Daniel Hartley</p>
      <p class="contact-role">Managing Director</p>
      <p class="contact-address">214 Harbor Lane, Suite 9<br>Eastfield Road EFD</p>
      <ul class="contact-lines">
        <li>012 555 0148
          <svg class="icon" viewBox="0 0 16 16"><path d="M3 1.5h3l1.2 3.3-1.8 1.2a8 8 0 0 0 4.6 4.6l1.2-1.8 3.3 1.2v3a1.5 1.5 0 0 1-1.6 1.5A13 13 0 0 1 1.5 3.1 1.5 1.5 0 0 1 3 1.5z"/></svg>
        </li>
        <li>012 555 0149
          <svg class="icon" viewBox="0 0 16 16"><rect x="4" y="1" width="8" height="14" rx="1.5"/><path d="M7 12.5h2"/></svg>
        </li>
        <li>info@brightcanyon.example
          <svg class="icon" viewBox="0 0 16 16"><rect x="1.5" y="3.5" width="13" height="9" rx="1"/><path d="M1.5 4l6.5 5 6.5-5"/></svg>
        </li>
        <li class="website">www.brightcanyoncleaner.example
          <svg class="icon" viewBox="0 0 16 16"><circle cx="8" cy="8" r="6.5"/><path d="M1.5 8h13M8 1.5c2.2 2 2.2 11 0 13M8 1.5c-2.2 2-2.2 11 0 13"/></svg>
        </li>
      </ul>
    </div>
  </section>

  <section class="card card-back" aria-label="Business card back">
    <div class="back-brand">
      <p class="brand-name">Bright Canyon</p>
      <p class="product-line">Waterless Cleaner &amp; Protectant</p>
      <p class="back-website">www.brightcanyoncleaner.example</p>
    </div>
    <div class="qr-space" role="img" aria-label="Space reserved for QR code"></div>
    <div class="retro-scene" role="img" aria-label="1950s hot rod truck towing a vintage travel trailer along a desert road"></div>
  </section>

</main>
</body>
</html>
```